KAY VELORE

We need a letterhead design for an Image & Etiquette Consultancy company based in Singapore.

The services we provide are Personal Image Consultation, Image & Etiquette Workshop for schools and corporate.

The design should have our corporate colour as seen in the logo files I have uploaded.

Since our company helps clients with their image, the design should be aesthetically very appealing. It should reflect a very classy & elegant feel.

I will print the letterhead using my printer but most of the time will use it to write letters to my clients therefore the format should include MS Word.

```html
<!DOCTYPE html>
<html lang="en">
<head>
<meta charset="utf-8">
<title>Kay Velore — Letterhead</title>
<link href="https://fonts.googleapis.com/css2?family=Michroma&family=Open+Sans:wght@400;600&display=swap" rel="stylesheet">
<style>
  :root {
    --backdrop: #ececec;
    --paper: #ffffff;
    --plum: #3d2352;
    --gold: #c39a2c;
    --gold-light: #e0c25a;
    --gold-deep: #a97f1f;
    --ink-soft: #6a6470;
  }
  * { box-sizing: border-box; margin: 0; padding: 0; }
  html, body {
    width: 1200px; height: 795px; overflow: hidden;
    background: var(--backdrop);
  }
  .letterhead {
    position: absolute;
    left: 330px; top: 16px;
    width: 540px; height: 763px;
    background: var(--paper);
    box-shadow: 0 2px 10px rgba(0,0,0,0.08);
  }
  .brand {
    position: absolute; left: 36px; top: 42px;
    width: 200px;
  }
  .brand-name {
    font-family: "Michroma", sans-serif;
    font-size: 18px; letter-spacing: 1px;
    color: var(--plum); font-weight: 400;
    line-height: 1; white-space: nowrap;
  }
  .brand-tagline {
    margin-top: 7px;
    font-family: "Open Sans", sans-serif;
    font-size: 7px; letter-spacing: 2.2px;
    text-transform: uppercase; color: var(--gold);
    white-space: nowrap;
  }
  .contact {
    position: absolute; right: 28px; top: 42px;
    display: flex; gap: 12px;
    font-family: "Open Sans", sans-serif;
    font-style: normal;
    font-size: 6.5px; line-height: 1.6; color: var(--ink-soft);
    white-space: nowrap;
  }
  .contact-group { display: flex; flex-direction: column; }
  .contact-line { display: flex; align-items: center; gap: 4px; }
  .contact-line svg { width: 6px; height: 6px; flex: none; fill: var(--gold); }
  .contact-line.indent { padding-left: 10px; }
  .footer-band {
    position: absolute; left: 0; right: 0; bottom: 26px; height: 14px;
    background: linear-gradient(90deg, var(--gold-deep) 0%, var(--gold) 30%, var(--gold-light) 55%, var(--gold) 80%, var(--gold-deep) 100%);
  }
  .footer-rule {
    position: absolute; left: 0; right: 0; bottom: 16px; height: 3px;
    background: var(--gold);
  }
</style>
</head>
<body>
  <main class="letterhead">
    <header class="brand">
      <div class="brand-name">KAY VELORE</div>
      <div class="brand-tagline">Grace in every detail</div>
    </header>

    <address class="contact">
      <div class="contact-group">
        <div class="contact-line">
          <svg viewBox="0 0 10 10"><path d="M5 0a3.5 3.5 0 0 0-3.5 3.5C1.5 6 5 10 5 10s3.5-4 3.5-6.5A3.5 3.5 0 0 0 5 0zm0 5a1.5 1.5 0 1 1 0-3 1.5 1.5 0 0 1 0 3z"/></svg>
          <span>What ever your street No.12</span>
        </div>
        <div class="contact-line indent">your city postal code</div>
      </div>
      <div class="contact-group">
        <div class="contact-line">
          <svg viewBox="0 0 10 10"><path d="M2 0.5l2 2.2-1 1.3c.6 1.3 1.7 2.4 3 3l1.3-1 2.2 2-1.2 1.5C4.5 9.2.8 5.5.5 1.7z"/></svg>
          <span>0 123 456 789</span>
        </div>
        <div class="contact-line">
          <svg viewBox="0 0 10 10"><rect x="2.5" y="0" width="5" height="10" rx="1"/></svg>
          <span>0 123 456 789</span>
        </div>
      </div>
      <div class="contact-group">
        <div class="contact-line">
          <svg viewBox="0 0 10 10"><path d="M0 2h10v6H0z M0 2l5 3.5L10 2" /></svg>
          <span>info@kayvelore.com</span>
        </div>
        <div class="contact-line">
          <svg viewBox="0 0 10 10"><circle cx="5" cy="5" r="5"/></svg>
          <span>www.kayvelore.com</span>
        </div>
      </div>
    </address>

    <div class="footer-band"></div>
    <div class="footer-rule"></div>
  </main>
</body>
</html>
```